Business Card and Stationary Designs for commercial construction company
Halvern Builders, Inc.
Creative Brief
Use standard fonts
Dennis Whitlock
Director of Operations
6387 Larkmeadow Lane Elk Grove, CA 95731
dennis.whitlock@halvernbldg.com
License #3084519
We like the colors of our logo, so please incorporate them into the card. The font for the other information on the business card does not have to match the logo font, but it should coordinate with it. We need the stationary design to be used to print actual stationary, but we would also like a word document that we can use for creating letters on electronic stationary.

```html
<!DOCTYPE html>
<html lang="en">
<head>
<meta charset="utf-8">
<title>Halvern Builders — Business Card</title>
<link href="https://fonts.googleapis.com/css2?family=Montserrat:wght@400;500;800&display=swap" rel="stylesheet">
<style>
  :root {
    --backdrop: #e9e9e9;
    --card-white: #ffffff;
    --panel-grey: #8c8c8c;
    --brand-red: #d8242c;
    --text-light: #ffffff;
    --text-soft: #f1f1f1;
  }
  html, body {
    margin: 0;
    width: 1200px;
    height: 901px;
    overflow: hidden;
    background: var(--backdrop);
    font-family: "Montserrat", Arial, sans-serif;
  }
  .business-card {
    position: absolute;
    left: 150px;
    top: 193px;
    width: 900px;
    height: 514px;
    border-radius: 28px;
    overflow: hidden;
    background: var(--card-white);
    box-shadow: 0 6px 24px rgba(0,0,0,0.12);
  }
  .card-shapes {
    position: absolute;
    inset: 0;
  }
  .brand-mark {
    position: absolute;
    left: 70px;
    top: 218px;
    display: flex;
    align-items: center;
    gap: 16px;
  }
  .brand-square {
    width: 44px;
    height: 44px;
    background: var(--brand-red);
  }
  .brand-name {
    font-weight: 800;
    font-size: 58px;
    letter-spacing: 1px;
    color: var(--brand-red);
    line-height: 1;
  }
  .contact-block {
    position: absolute;
    right: 42px;
    top: 110px;
    text-align: right;
    color: var(--text-light);
  }
  .person-name {
    font-size: 27px;
    font-weight: 500;
    letter-spacing: 1px;
    margin: 0;
  }
  .person-title {
    font-size: 16px;
    margin: 4px 0 0;
    color: var(--text-soft);
  }
  .postal-address {
    font-style: normal;
    font-size: 16px;
    line-height: 1.5;
    margin-top: 48px;
  }
  .contact-lines {
    list-style: none;
    margin: 34px 0 0;
    padding: 0;
    font-size: 15px;
  }
  .contact-lines li {
    display: flex;
    justify-content: flex-end;
    align-items: center;
    gap: 12px;
    height: 30px;
  }
  .contact-lines svg {
    width: 16px;
    height: 16px;
    fill: var(--text-light);
  }
</style>
</head>
<body>
  <div class="business-card">
    <svg class="card-shapes" viewBox="0 0 900 514" preserveAspectRatio="none" aria-hidden="true">
      <path d="M540 0 C440 120 480 260 430 360 C400 420 390 480 380 514 L900 514 L900 0 Z" fill="var(--panel-grey)"/>
      <path d="M500 0 L548 0 C455 100 475 220 425 330 C455 225 430 110 500 0 Z" fill="var(--brand-red)"/>
    </svg>

    <div class="brand-mark">
      <span class="brand-square"></span>
      <span class="brand-name">HALVERN</span>
    </div>

    <div class="contact-block">
      <h1 class="person-name">DENNIS WHITLOCK</h1>
      <p class="person-title">Director of Operations</p>
      <address class="postal-address">6387 Larkmeadow Lane<br>Elk Grove, CA 95731</address>
      <ul class="contact-lines">
        <li>916 555 0142
          <svg viewBox="0 0 24 24"><path d="M6.6 10.8a15 15 0 0 0 6.6 6.6l2.2-2.2c.3-.3.7-.4 1-.2 1.1.4 2.3.6 3.6.6.6 0 1 .4 1 1V20c0 .6-.4 1-1 1A17 17 0 0 1 3 4c0-.6.4-1 1-1h3.5c.6 0 1 .4 1 1 0 1.3.2 2.5.6 3.6.1.3 0 .7-.2 1z"/></svg>
        </li>
        <li>916 555 0143
          <svg viewBox="0 0 24 24"><path d="M7 1h10a2 2 0 0 1 2 2v18a2 2 0 0 1-2 2H7a2 2 0 0 1-2-2V3a2 2 0 0 1 2-2zm0 3v14h10V4zm5 15.5a1 1 0 1 0 0 2 1 1 0 0 0 0-2z"/></svg>
        </li>
        <li>916 555 0144
          <svg viewBox="0 0 24 24"><path d="M6 2h9l4 4v6H6zm-2 11h16a2 2 0 0 1 2 2v6H2v-6a2 2 0 0 1 2-2zm2 3v2h4v-2z"/></svg>
        </li>
        <li>dennis.whitlock@halvernbldg.com
          <svg viewBox="0 0 24 24"><path d="M2 5h20v14H2zm2 2v.5l8 5 8-5V7l-8 5z"/></svg>
        </li>
        <li>www.halvernbldg.com
          <svg viewBox="0 0 24 24"><path d="M12 2a10 10 0 1 0 0 20 10 10 0 0 0 0-20zm0 2c1 0 2.3 2 2.8 5H9.2C9.7 6 11 4 12 4zM4.3 11h3.8a16 16 0 0 0 0 2H4.3a8 8 0 0 1 0-2zm5 0h5.4a14 14 0 0 1 0 2H9.3a14 14 0 0 1 0-2zm6.6 0h3.8a8 8 0 0 1 0 2h-3.8a16 16 0 0 0 0-2zM9.2 15h5.6c-.5 3-1.8 5-2.8 5s-2.3-2-2.8-5z"/></svg>
        </li>
      </ul>
    </div>
  </div>
</body>
</html>
```